A resume/portfolio website for myself

I'm an independent software contractor, architect, tech trainer. I need a web site to present myself. Many ready to use portfolio designs are too artistic and focused on presenting design skills of the person. I like a nice website but the content should be a little less graphic than if you would present a graphic designer. Content could be presentation of me, core skill qualities and services and resume. Potentially a page with my tech courses in the longer run

```html
<!DOCTYPE html>
<html lang="en">
<head>
<meta charset="utf-8">
<title>Daniel — Software, Architecture &amp; Technology</title>
<link href="https://fonts.googleapis.com/css2?family=Montserrat:ital,wght@0,400;0,500;0,600;0,700;1,400&display=swap" rel="stylesheet">
<style>
:root{
  --ink:#333338;
  --text:#4a4a50;
  --muted:#6b6b72;
  --accent:#1a6fb0;
  --accent-soft:#8ab8d6;
  --band:#e4e4ea;
  --white:#ffffff;
}
*{box-sizing:border-box;margin:0;padding:0}
html,body{width:1200px;height:2446px;overflow:hidden;background:var(--white)}
body{position:relative;font-family:"Montserrat",sans-serif;color:var(--ink)}
a{color:inherit;text-decoration:none}

.site-header{position:absolute;top:0;left:0;width:1200px;height:70px}
.brand{position:absolute;left:149px;top:20px;font-size:23px;font-weight:400;letter-spacing:1px}
.main-nav{position:absolute;top:28px;left:0;width:1200px;font-size:14px;font-weight:500;letter-spacing:.6px}
.main-nav a{position:absolute;white-space:nowrap}

.hero{position:absolute;top:0;left:0;width:1200px;height:676px;overflow:hidden}
.hero-art{position:absolute;top:0;left:0}
.hero-portrait{position:absolute;left:759px;top:152px;width:340px;height:447px;border-radius:170px 170px 0 0;
  background:linear-gradient(180deg,#c9b8a8 0%,#3f5a80 38%,#2b4468 100%)}
.hero-greeting{position:absolute;left:149px;top:212px;font-size:22px;font-weight:400;letter-spacing:.8px}
.hero-title{position:absolute;left:149px;top:250px;width:520px;font-size:40px;line-height:46.5px;font-weight:700;letter-spacing:.3px}

.category-band{position:absolute;top:599px;left:0;width:1200px;height:76px;background:var(--band)}
.category-nav a{position:absolute;top:28px;font-size:15px;font-weight:500;letter-spacing:.6px}
.category-nav a.is-active{color:var(--accent)}

.post-card{position:absolute;width:285px}
.post-image{width:285px;height:225px}
.post-title{margin-top:27px;font-size:19.5px;line-height:23px;font-weight:500;letter-spacing:.6px;color:var(--ink)}
.post-excerpt{margin-top:4px;font-size:15px;line-height:22.4px;color:var(--muted);letter-spacing:.1px}
.post-more{display:block;margin-top:4px;font-size:15px;font-weight:600;color:var(--ink)}

.img-house{background:linear-gradient(135deg,#6d7d73 0%,#8a9a86 45%,#c69a6a 75%,#3d4a3e 100%)}
.img-white{background:linear-gradient(135deg,#eef1f3 0%,#dfe5ea 50%,#bcd0dd 100%)}
.img-wave{background:linear-gradient(170deg,#0a7ea3 0%,#0a7ea3 45%,#9fb8c3 75%,#dfe8ec 100%)}
.img-curve{background:linear-gradient(135deg,#7a95ad 0%,#a9bccd 40%,#5e7388 70%,#c7d4df 100%)}
.img-green{background:linear-gradient(180deg,#6a9b3a 0%,#8d8e86 35%,#7aa94a 65%,#6c6d68 100%)}
.img-fins{background:linear-gradient(120deg,#b7cbd0 0%,#e6eeef 50%,#f7f9fa 100%)}

.pagination{position:absolute;top:2014px;left:0;width:1200px;font-size:16px;font-weight:600}
.pagination a{position:absolute}
.pagination .prev{color:var(--muted);font-weight:500}
.pagination .current{color:var(--accent)}

.subscribe{position:absolute;top:2059px;left:0;width:1200px;height:219px;background:var(--band);border-bottom:3px solid var(--accent)}
.subscribe-title{position:absolute;left:149px;top:52px;font-size:31px;font-weight:600;letter-spacing:.5px}
.subscribe-title::after{content:"";position:absolute;left:0;top:47px;width:160px;height:4px;background:var(--accent)}
.subscribe-text{position:absolute;left:150px;top:113px;width:300px;font-size:15.5px;line-height:22px;letter-spacing:.2px}
.subscribe-input{position:absolute;left:584px;top:109px;width:300px;height:45px;border:1px solid #d5d5da;background:#efefef;
  font:italic 14px "Montserrat",sans-serif;color:#666;padding-left:15px;box-shadow:0 1px 2px rgba(0,0,0,.12)}
.subscribe-button{position:absolute;left:900px;top:109px;width:150px;height:45px;border:0;background:var(--accent);
  color:var(--white);font:500 14px "Montserrat",sans-serif}

.site-footer{position:absolute;top:2281px;left:0;width:1200px;height:165px}
.social-link{position:absolute;top:32px;width:57px;height:57px;border-radius:50%;background:var(--accent);color:var(--white);
  font-size:9.5px;font-weight:600;display:flex;align-items:center;justify-content:center}
.copyright{position:absolute;top:107px;left:0;width:1200px;text-align:center;font-size:15px;letter-spacing:.2px}
</style>
</head>
<body>

<section class="hero">
  <svg class="hero-art" width="1200" height="676" viewBox="0 0 1200 676" aria-hidden="true">
    <defs><clipPath id="above-band"><rect x="0" y="0" width="1200" height="599"/></clipPath></defs>
    <g clip-path="url(#above-band)">
      <circle cx="930" cy="479" r="290" fill="#e4e4ea"/>
      <circle cx="930" cy="479" r="310" fill="none" stroke="#8ab8d6" stroke-width="5"/>
    </g>
    <line x1="0" y1="596" x2="646" y2="596" stroke="#8ab8d6" stroke-width="5"/>
  </svg>
  <div class="hero-portrait" role="img" aria-label="Portrait photo of a smiling man with glasses in a denim shirt, arms crossed"></div>
  <p class="hero-greeting">Hi, I’m Daniel</p>
  <h1 class="hero-title">Here I share my thoughts about software, architecture, and technology.</h1>
</section>

<header class="site-header">
  <a class="brand" href="#">Logo</a>
  <nav class="main-nav">
    <a href="#" style="left:503px">Home</a>
    <a href="#" style="left:590px">About</a>
    <a href="#" style="left:680px">Services</a>
    <a href="#" style="left:784px">Skills</a>
    <a href="#" style="left:866px">Experience</a>
    <a href="#" style="left:992px">Contact</a>
  </nav>
</header>

<nav class="category-band category-nav">
  <a href="#" style="left:390px">Recent</a>
  <a href="#" style="left:477px">Software</a>
  <a href="#" class="is-active" style="left:586px">Architecture</a>
  <a href="#" style="left:723px">Technology</a>
</nav>

<main class="posts">
  <article class="post-card" style="left:150px;top:734px">
    <div class="post-image img-house" role="img" aria-label="Modern family house at dusk"></div>
    <h2 class="post-title">Architecture and the family: The need for privacy</h2>
    <p class="post-excerpt">Sed condimentum commodo nulla a interdum. Morbi in fringilla mi. Praesent id tortor lacinia.</p>
    <a class="post-more" href="#">Read More</a>
  </article>
  <article class="post-card" style="left:457px;top:734px">
    <div class="post-image img-white" role="img" aria-label="White residential building against a pale sky"></div>
    <h2 class="post-title">Trends of Environmental Technology in Residential</h2>
    <p class="post-excerpt">Sed condimentum commodo nulla a interdum. Morbi in fringilla mi. Praesent id tortor lacinia.</p>
    <a class="post-more" href="#">Read More</a>
  </article>
  <article class="post-card" style="left:765px;top:734px">
    <div class="post-image img-wave" role="img" aria-label="Wavy woven facade under a teal sky"></div>
    <h2 class="post-title">Creative Designs in the Modern Era</h2>
    <p class="post-excerpt">Sed condimentum commodo nulla a interdum. Morbi in fringilla mi. Praesent id tortor lacinia.</p>
    <a class="post-more" href="#">Read More</a>
  </article>

  <article class="post-card" style="left:150px;top:1160px">
    <div class="post-image img-curve" role="img" aria-label="Curved steel building facade"></div>
    <h2 class="post-title">Retaining Green Cities in Periods of Growth</h2>
    <p class="post-excerpt">Sed condimentum commodo nulla a interdum. Morbi in fringilla mi. Praesent id tortor lacinia.</p>
    <a class="post-more" href="#">Read More</a>
  </article>
  <article class="post-card" style="left:457px;top:1160px">
    <div class="post-image img-green" role="img" aria-label="Building terraces covered with green plants"></div>
    <h2 class="post-title">Maximizing Green Space in Residential Designs</h2>
    <p class="post-excerpt">Sed condimentum commodo nulla a interdum. Morbi in fringilla mi. Praesent id tortor lacinia.</p>
    <a class="post-more" href="#">Read More</a>
  </article>
  <article class="post-card" style="left:765px;top:1160px">
    <div class="post-image img-fins" role="img" aria-label="White vertical fins of a modern structure"></div>
    <h2 class="post-title">Applications of Hemp in Building Structure</h2>
    <p class="post-excerpt">Sed condimentum commodo nulla a interdum. Morbi in fringilla mi. Praesent id tortor lacinia.</p>
    <a class="post-more" href="#">Read More</a>
  </article>

  <article class="post-card" style="left:150px;top:1586px">
    <div class="post-image img-house" role="img" aria-label="Modern family house at dusk"></div>
    <h2 class="post-title">Architecture and the family: The need for privacy</h2>
    <p class="post-excerpt">Sed condimentum commodo nulla a interdum. Morbi in fringilla mi. Praesent id tortor lacinia.</p>
    <a class="post-more" href="#">Read More</a>
  </article>
  <article class="post-card" style="left:457px;top:1586px">
    <div class="post-image img-white" role="img" aria-label="White residential building against a pale sky"></div>
    <h2 class="post-title">Trends of Environmental Technology in Residential</h2>
    <p class="post-excerpt">Sed condimentum commodo nulla a interdum. Morbi in fringilla mi. Praesent id tortor lacinia.</p>
    <a class="post-more" href="#">Read More</a>
  </article>
  <article class="post-card" style="left:765px;top:1586px">
    <div class="post-image img-wave" role="img" aria-label="Wavy woven facade under a teal sky"></div>
    <h2 class="post-title">Creative Designs in the Modern Era</h2>
    <p class="post-excerpt">Sed condimentum commodo nulla a interdum. Morbi in fringilla mi. Praesent id tortor lacinia.</p>
    <a class="post-more" href="#">Read More</a>
  </article>
</main>

<nav class="pagination">
  <a class="prev" href="#" style="left:498px">Previous</a>
  <a class="current" href="#" style="left:589px">1</a>
  <a href="#" style="left:609px">2</a>
  <a href="#" style="left:632px">3</a>
  <a href="#" style="left:664px">Next</a>
</nav>

<section class="subscribe">
  <h2 class="subscribe-title">Subscribe</h2>
  <p class="subscribe-text">Subscribe to the newsletter to stay updated with the latest blog posts.</p>
  <input class="subscribe-input" type="email" placeholder="Enter your email">
  <button class="subscribe-button" type="button">Subscribe</button>
</section>

<footer class="site-footer">
  <a class="social-link" href="#" style="left:466px">Friendly</a>
  <a class="social-link" href="#" style="left:537px">Chirper</a>
  <a class="social-link" href="#" style="left:607px">Snapgram</a>
  <a class="social-link" href="#" style="left:677px">ProLink</a>
  <p class="copyright">Website name 2020 © All Rights Reserved</p>
</footer>

</body>
</html>
```